prestige web design for KELVA Finance

Hi Guys,

Looking to team up with a creative designer for another of our websites for KELVA finance.
if looking for our similar website www.brimlendco.com.au is one of our other companies. ideally working in our logo being black and white.

Please see attachments for our logo and a description
HOME
VEHICLE
EQUIPMENT
WHO WE ARE
CONTACT US

open to ideas on layout .

touch base if you have any questions.

Target Market(s)

Prestige cars and equipment -trucks earthmoving

Industry/Entity Type

finance

Coding

Coded - Design and coding required

Number of Pages Required

5+ page

Font styles to use
Sans Serif

Colors

Designer to choose colors to be used in the design.

```html
<!DOCTYPE html>
<html lang="en">
<head>
<meta charset="utf-8">
<title>KELVA Finance</title>
<link href="https://fonts.googleapis.com/css2?family=DM+Sans:wght@400;500;700&display=swap" rel="stylesheet">
<style>
:root{
  --blue:#0b7df0;
  --red:#f24c4c;
  --ink:#141414;
  --text:#3a3f44;
  --light:#eef1f5;
  --dark:#232f38;
  --footer:#0f151a;
  --white:#ffffff;
}
*{box-sizing:border-box;margin:0;padding:0}
html,body{width:1200px;height:2808px;overflow:hidden;background:#fff;font-family:"DM Sans",sans-serif;color:var(--text)}
.page{position:absolute;left:0;top:45px;width:1200px;height:2718px}
.abs{position:absolute}

/* hero */
.hero{left:0;top:0;width:1200px;height:437px;background:linear-gradient(120deg,#3b3430 0%,#5a4a3c 45%,#3a3532 75%,#2a2a2c 100%)}
.logo{font-weight:500;color:var(--white);font-size:30px;letter-spacing:.5px}
.hero .logo{left:200px;top:22px}
.nav{left:564px;top:38px;display:flex;gap:30px;align-items:center;font-size:11px;font-weight:700;color:var(--white)}
.nav .active{color:var(--red)}
.nav .cta{background:var(--blue);padding:8px 17px;margin-left:-4px}
.headline{left:0;width:1200px;top:140px;text-align:center;color:var(--white);font-size:45px;font-weight:500;line-height:1.18}

/* intro */
.intro{left:0;top:437px;width:1200px;height:450px;background:var(--light)}
.side-logo{left:36px;top:610px;transform:rotate(-90deg);transform-origin:center;color:var(--ink);font-size:40px;font-weight:500;white-space:nowrap;width:240px;text-align:center}
.h2{color:var(--ink);font-weight:500}
.makers{left:200px;top:534px;font-size:30px}
.para{font-size:12px;line-height:22.5px}
.makers-text{left:200px;top:578px;width:460px}
.btn{display:inline-block;font-size:11px;font-weight:700;color:var(--white);padding:9px 18px}
.btn-red{background:var(--red)}
.btn-blue{background:var(--blue)}

/* calculator */
.calc{left:686px;top:313px;width:314px;height:574px;background:var(--blue);color:var(--white);padding:18px 30px}
.calc h3{text-align:center;font-size:18px;font-weight:500;line-height:22px;margin-bottom:20px}
.calc label{display:block;font-size:10.5px;margin-bottom:8px}
.field{background:var(--white);height:24px;margin-bottom:15px;color:var(--ink);font-size:10px;padding:6px 12px;display:flex;justify-content:space-between}
.calc-btn{display:block;margin:4px auto 14px;background:#000;color:#fff;width:100px;text-align:center;font-size:12px;font-weight:700;padding:7px 0}
.calc .center{text-align:center}
.disclaimer{font-size:9px;line-height:13px;text-align:center;margin-top:22px}
.disclaimer b{display:block}

/* why */
.why-title{left:0;width:1200px;top:940px;text-align:center;font-size:37px}
.why-sub{left:380px;width:440px;top:990px;text-align:center;font-size:11px;line-height:14px;color:var(--ink)}
.photo{}
.car{left:612px;top:1068px;width:388px;height:280px;background:linear-gradient(160deg,#c98b4a 0%,#7b6b5c 40%,#8c949b 65%,#1f4a6a 100%)}
.loan-title{left:200px;top:1140px;font-size:21px}
.loan-text{left:200px;top:1173px;width:360px;font-size:12px;line-height:16px;color:var(--ink)}
.loan-btn{left:200px;top:1228px}

.band{left:0;top:1411px;width:1200px;height:281px;background:var(--light)}
.loader{left:200px;top:1411px;width:387px;height:281px;background:linear-gradient(180deg,#5f86b6 0%,#a3b8cc 40%,#cfb387 70%,#b0946a 100%)}
.equip-title{left:637px;top:1473px;font-size:21px}
.equip-text{left:637px;top:1507px;width:360px;font-size:11.5px;line-height:18px;color:var(--ink)}
.equip-text a{color:var(--blue);text-decoration:none}
.equip-btn{left:637px;top:1580px}

.about-logo{left:200px;top:1787px;color:var(--ink);font-size:28px;font-weight:500}
.about-text{left:200px;top:1842px;width:390px;font-size:11.5px;line-height:18.5px;color:var(--ink)}
.about-btn{left:200px;top:2038px}
.office{left:612px;top:1753px;width:388px;height:344px;background:linear-gradient(135deg,#9aa7b3 0%,#d9dde2 45%,#ece7e2 70%,#b9b6b3 100%)}

/* contact */
.contact{left:0;top:2161px;width:1200px;height:509px;background:var(--dark);color:var(--white)}
.contact-title{left:0;width:1200px;top:2191px;text-align:center;font-size:37px;font-weight:500;color:var(--white)}
.contact-text{left:0;width:1200px;top:2249px;text-align:center;font-size:13px;line-height:22px;color:var(--white)}
.input{background:var(--white);height:29px;font-size:9.5px;color:var(--ink);padding:9px 12px}
.send{left:556px;top:2599px;width:87px;height:29px;background:var(--blue);color:#fff;font-size:11px;font-weight:700;text-align:center;line-height:29px}
.footer{left:0;top:2670px;width:1200px;height:47px;background:var(--footer);color:var(--white);font-size:10px;text-align:center;line-height:47px}
.footer .brand{color:var(--blue)}
.footer .sep{margin:0 10px}
</style>
</head>
<body>
<div class="page">

  <section class="abs hero" role="img" aria-label="Photo of a person writing on financial charts beside a laptop on a wooden desk"></section>
  <div class="abs logo">KELVA Finance</div>
  <nav class="abs nav">
    <span class="active">Home</span><span>Vehicle</span><span>Equipment</span><span>Who We Are</span><span class="cta">Contact Us</span>
  </nav>
  <h1 class="abs headline">Connecting all your<br>banking needs</h1>

  <section class="abs intro"></section>
  <div class="abs side-logo">KELVA Finance</div>
  <h2 class="abs h2 makers">Makers of possible</h2>
  <div class="abs para makers-text">
    <p>KELVA Finance has nearly 20 years industry experience, so we certainly understand personal and business lending. We are committed to providing individuals and businesses with tailored financial services that enable them to reach and then exceed their financial goals.&nbsp; We have a vast list of lenders to suit along with an online team ready to help you, so we're easily accessible and here when you need us. Our friendly team of experienced and approachable staff that will listen, understand your situation and lend responsibly.</p>
    <span class="btn btn-red" style="margin-top:25px">Contact Us</span>
  </div>

  <aside class="abs calc">
    <h3>Finance Repayment<br>Calculator</h3>
    <label>Purchase amount:</label><div class="field">$</div>
    <label>Diposit:</label><div class="field">$</div>
    <label>Term: &#9432;</label><div class="field"><span>3 years</span><span>&#8964;</span></div>
    <label>Interest Rate % p.a: &#9432;</label><div class="field">7.5</div>
    <label>Balloon Payment: &#9432;</label><div class="field">$</div>
    <span class="calc-btn">Calculate</span>
    <label class="center">Repayment Monthly: &#9432;</label><div class="field"></div>
    <p class="disclaimer"><b>Disclaimer</b>Lorem Ipsum is simply dummy text of the printing and typesetting industry. Lorem Ipsum has been the industry's standard dummy text ever since.</p>
  </aside>

  <h2 class="abs h2 why-title">Why choose us?</h2>
  <p class="abs why-sub">Well, because we're here to help you! We care about outcomes and helping you achieve a stress and enjoyable lending experience.</p>

  <h3 class="abs h2 loan-title">Vehicle loan</h3>
  <p class="abs loan-text">While you focus on getting the right car, we will focus on getting you the right finance.</p>
  <span class="abs btn btn-blue loan-btn">Apply Now!</span>
  <div class="abs car" role="img" aria-label="Photo of a silver sports sedan on a desert road at sunset"></div>

  <section class="abs band"></section>
  <div class="abs loader" role="img" aria-label="Photo of a yellow wheel loader at a construction site under a blue sky"></div>
  <h3 class="abs h2 equip-title">Equipment</h3>
  <p class="abs equip-text">At KELVA, we help businesses of all sizes to secure funding in the form of a business loan for asset purchases from either a bank or private lender... <a>[Read more]</a></p>
  <span class="abs btn btn-red equip-btn">Apply Now!</span>

  <div class="abs about-logo">KELVA Finance</div>
  <div class="abs about-text">
    <p>The goal of <b>KELVA Finance</b> is to build on the track record of the KELVA business and to create a new benchmark in the Australia's Asset Finance industry, providing good old fashioned localised service that delivers the assets you want when you need them and structured to recognise asset useful life while being sensitive to cashflow.</p>
    <p style="margin-top:18px">Providing second to none asset finance support to business owners and individuals alike ...</p>
  </div>
  <span class="abs btn btn-red about-btn">Who We Are</span>
  <div class="abs office" role="img" aria-label="Photo of a businesswoman using a calculator beside a laptop"></div>

  <section class="abs contact"></section>
  <h2 class="abs contact-title">Contact us</h2>
  <p class="abs contact-text">To find out how to get KELVA Finance working for you helping with your funding needs.<br><b>Please call 13 58 82&nbsp; ( 13 KELVA)</b><br>Or Contact us now: Alternatively send us a message with your questions.</p>
  <div class="abs input" style="left:296px;top:2376px;width:297px">First Name</div>
  <div class="abs input" style="left:606px;top:2376px;width:301px">Last Name</div>
  <div class="abs input" style="left:296px;top:2420px;width:297px">Phone</div>
  <div class="abs input" style="left:606px;top:2420px;width:301px">Regional Location</div>
  <div class="abs input" style="left:296px;top:2464px;width:297px">Email</div>
  <div class="abs input" style="left:606px;top:2464px;width:301px">Subject</div>
  <div class="abs input" style="left:296px;top:2509px;width:611px;height:73px">Message</div>
  <div class="abs send">Send</div>

  <footer class="abs footer">&copy; 2022 <span class="brand">KELVA Finance.</span> All Rights Reserved<span class="sep">I</span>Terms and Conditions<span class="sep">I</span>Privacy Policy</footer>
</div>
</body>
</html>
```